Embroidery Teacher

I design and teach small embroidery classes, I am based in South Australia
The majority of my embroidery is done on bright wool fabrics and the designs are naive / folk art type birds, flowers and houses. The finished products stitched by the ladies in my classes are usually made into book covers, needle keepers or small quilts.

Industry/Entity Type

Embroidery

Contact Information for Business Card

Rosalind Hatchett
PO Box 3817
Fernvale SA 5092
M. 0427183592
E. ros@merrythreadwork.com.au

```html
<!DOCTYPE html>
<html lang="en">
<head>
<meta charset="utf-8">
<title>Merry Threadwork – Business Card</title>
<link rel="stylesheet" href="https://fonts.googleapis.com/css2?family=Montserrat:wght@400;500&display=swap">
<style>
  :root {
    --backdrop: #e9e4dc;
    --card-white: #ffffff;
    --orange: #ee8a1c;
    --orange-deep: #d9700f;
    --plum: #2e1420;
    --berry: #b8284f;
    --ink: #3a2a2a;
    --shadow: rgba(40, 25, 10, 0.25);
  }
  * { box-sizing: border-box; margin: 0; padding: 0; }
  html, body {
    width: 1200px;
    height: 1023px;
    overflow: hidden;
    background: var(--backdrop);
    font-family: "Montserrat", sans-serif;
  }
  .sheet {
    width: 1200px;
    height: 1023px;
    display: flex;
    flex-direction: column;
    align-items: center;
    justify-content: center;
    gap: 70px;
  }
  .card {
    position: relative;
    width: 700px;
    height: 400px;
    overflow: hidden;
    box-shadow: 0 10px 30px var(--shadow);
  }
  /* Front */
  .card-front { background: var(--orange); }
  .card-front .stitch-artwork {
    position: absolute;
    inset: 0;
    background:
      linear-gradient(160deg, #f49a2a 0%, var(--orange) 35%, #c8553a 60%, var(--orange-deep) 100%);
  }
  .card-front .side-band {
    position: absolute;
    top: 0;
    right: 0;
    width: 190px;
    height: 100%;
  }
  /* Back */
  .card-back { background: var(--card-white); }
  .card-back .edge-band {
    position: absolute;
    left: 0;
    top: 0;
    width: 34px;
    height: 100%;
    background: var(--orange);
  }
  .card-back .rule {
    position: absolute;
    left: 470px;
    top: 0;
    width: 4px;
    height: 100%;
    background: var(--orange);
  }
  .contact {
    position: absolute;
    left: 90px;
    top: 90px;
    color: var(--ink);
    font-size: 19px;
    line-height: 1.7;
    font-weight: 400;
  }
  .contact .name {
    font-weight: 500;
    font-size: 26px;
    color: var(--plum);
    margin-bottom: 14px;
  }
  .contact .label { color: var(--orange-deep); font-weight: 500; }
  .web {
    position: absolute;
    left: 496px;
    top: 0;
    height: 100%;
    display: flex;
    align-items: center;
    justify-content: center;
    writing-mode: vertical-rl;
    font-size: 16px;
    color: var(--ink);
    white-space: nowrap;
  }
</style>
</head>
<body>
<main class="sheet">
  <section class="card card-front">
    <div class="stitch-artwork" role="img" aria-label="Photograph of two embroidered folk-art birds in bright wool on orange fabric"></div>
    <svg class="side-band" viewBox="0 0 190 400" preserveAspectRatio="none" aria-hidden="true">
      <path d="M190 0 L150 0 C150 80 60 110 60 200 L60 400 L190 400 Z" fill="var(--plum)"/>
    </svg>
  </section>

  <section class="card card-back">
    <div class="edge-band"></div>
    <div class="rule"></div>
    <div class="contact">
      <p class="name">Rosalind Hatchett</p>
      <p>PO Box 3817</p>
      <p>Fernvale SA 5092</p>
      <p><span class="label">M.</span> 0427183592</p>
      <p><span class="label">E.</span> ros@merrythreadwork.com.au</p>
    </div>
    <p class="web">merrythreadwork.com.au</p>
  </section>
</main>
</body>
</html>
```